A website for a Maltese Law Firm

Our law firm needs a website to further its business. The site should have a simple yet effective design. We would need the following sections: About us, Practice Areas, About Malta, Contact. These should be further split as follows:

About us: Our firm, Our values, What others say, Offices

Practice Areas: Crimimal, Citizenship & Residence, Overseas Patron Scheme, Criminal Defence, Civil Litigation, Arbitration and ADR, Commercial and Corporate, Media Law.

About Malta: just one section.

Contact: Just one section

We would also need a news feed at the front of the site to include latest news regarding our cases.

At the bottom we need a section for our Terms and a Privacy Statement.

Our logo is being attached.

Target Market(s)

All clients looking for legal assistance in Malta

Industry/Entity Type

Legal

Coding

Coded - Design and coding required

Number of Pages Required

1 page

Requirements
Must have
• It must be simple yet striking.

```html
<!DOCTYPE html>
<html lang="en">
<head>
<meta charset="utf-8">
<title>Moravia &amp; Zammit — Advocates, Malta</title>
<link rel="stylesheet" href="https://fonts.googleapis.com/css2?family=Raleway:wght@300;400;500;600;700;800&display=swap">
<style>
:root{
  --ink:#1f1f1f;
  --text:#333;
  --muted:#666;
  --dark:#2a2624;
  --darker:#231f1d;
  --white:#fff;
  --line:#d6d6d6;
  --foot:#2b2b2b;
  --foot-bar:#474747;
}
*{box-sizing:border-box;margin:0;padding:0}
html,body{width:1200px;height:2903px;overflow:hidden}
body{font-family:"Raleway",Arial,sans-serif;color:var(--text);background:var(--white);position:relative}
.section{position:absolute;left:0;width:1200px;overflow:hidden}

/* header */
.site-header{top:0;height:72px;background:var(--white)}
.brand{position:absolute;left:248px;top:22px;font-size:21px;font-weight:600;letter-spacing:1px;color:var(--ink);border-bottom:1px solid var(--ink);padding-bottom:3px}
.contact-bit{position:absolute;top:26px;display:flex;gap:8px;font-size:10px;font-weight:600;color:var(--ink);line-height:13px}
.contact-bit svg{width:20px;height:20px;fill:#8a8a8a}
.contact-phone{left:660px}
.contact-address{left:798px}

/* nav */
.main-nav{top:72px;height:40px;background:var(--darker)}
.main-nav ul{list-style:none;position:absolute;left:252px;top:0;display:flex;gap:38px;height:40px;align-items:center}
.main-nav li{font-size:11.5px;font-weight:600;color:var(--white)}
.main-nav .caret{font-size:8px;margin-left:4px}
.social{position:absolute;left:838px;top:8px;display:flex;gap:6px}
.social span{width:24px;height:24px;border-radius:50%;background:#8d8d8d}
.social span:first-child{background:var(--white)}
.dropdown{position:absolute;left:312px;top:112px;width:137px;height:124px;background:var(--darker);z-index:3;padding:18px 0 0 16px;list-style:none}
.dropdown li{font-size:9.5px;font-weight:600;color:var(--white);line-height:24px}

/* hero */
.hero{top:112px;height:459px}
.hero-photo{position:absolute;inset:0;background:linear-gradient(90deg,#cbb9a4 0%,#b4977b 28%,#8e7b6c 55%,#c7b29c 80%,#d9c7b3 100%)}
.hero-shade{position:absolute;inset:0;background:linear-gradient(90deg,rgba(0,0,0,.45),rgba(0,0,0,.1) 55%,rgba(0,0,0,0))}
.hero-copy{position:absolute;left:265px;top:158px;color:var(--white)}
.hero-copy h1{font-size:27px;font-weight:700;letter-spacing:.5px;margin-bottom:12px}
.hero-copy li{list-style:none;font-size:18px;font-weight:700;line-height:26.5px}
.btn{display:inline-block;border:1px solid var(--line);font-size:11px;font-weight:500;letter-spacing:.5px;padding:8px 12px;color:var(--ink);background:var(--white)}
.btn b{font-weight:800}
.btn.on-dark{background:transparent;color:var(--white);border-color:#bbb}
.hero .btn{position:absolute;left:265px;top:345px;background:rgba(0,0,0,.35);color:var(--white);border-color:#ddd;padding:8px 14px}
.dots{position:absolute;display:flex;gap:5px}
.dots i{width:5px;height:5px;border-radius:50%;background:var(--white)}
.hero .dots{left:580px;top:441px}

/* shared text column */
.eyebrow{font-size:15px;font-weight:300;color:var(--muted);letter-spacing:.5px;line-height:16px}
.section-name{font-size:17px;font-weight:700;color:var(--ink);letter-spacing:.3px;line-height:20px;margin-bottom:16px}
.body-copy{font-size:9.5px;line-height:12px;color:#444;margin-bottom:10px}
.copy-col .btn{margin-top:6px}

/* welcome */
.welcome{top:571px;height:296px}
.welcome-photo{position:absolute;left:248px;top:0;width:352px;height:296px;background:linear-gradient(135deg,#d9e1ea,#7f8fa3 45%,#2f3a4a 80%);clip-path:polygon(18px 0,100% 0,95% 100%,0 100%)}
.welcome .copy-col{position:absolute;left:631px;top:36px;width:322px}

/* practice */
.practice{top:867px;height:362px}
.dark-photo{position:absolute;inset:0;background:radial-gradient(ellipse at 80% 40%,#5a4a3e,#2b2420 60%,#1e1a18)}
.band-title{position:absolute;left:0;width:1200px;text-align:center;font-size:22px;font-weight:400;color:var(--white);letter-spacing:.5px}
.band-title b{font-weight:800}
.band-title::after{content:"";display:block;width:100px;height:2px;background:var(--white);margin:10px auto 0}
.practice .band-title{top:50px}
.practice-lead{position:absolute;left:248px;width:704px;top:138px;text-align:center;color:var(--white);font-size:16px;font-weight:600;line-height:21px}
.practice-more{position:absolute;left:268px;width:664px;top:196px;text-align:center;color:#eee;font-size:15px;font-weight:400;line-height:21px}
.practice-more b{font-weight:800;color:var(--white)}
.practice .btn{position:absolute;left:548px;top:290px}

/* about malta */
.about{top:1229px;height:298px}
.about .copy-col{position:absolute;left:248px;top:36px;width:322px}
.about h2{font-size:17px;font-weight:800;color:var(--ink);line-height:19px}
.about .eyebrow{margin-bottom:16px}
.about-photo{position:absolute;left:580px;top:0;width:368px;height:298px;background:linear-gradient(120deg,#eef1f3,#c8cfd4 40%,#5b4a40 70%,#2b2522);clip-path:polygon(30px 0,100% 0,100% 100%,0 100%)}

/* news */
.news{top:1527px;height:282px}
.news .band-title{top:40px}
.news-list{position:absolute;left:262px;top:124px;display:flex}
.news-item{width:236px;display:flex;gap:12px;color:var(--white)}
.news-item + .news-item{border-left:1px solid #777;padding-left:18px}
.news-date{font-size:34px;font-weight:300;line-height:32px;width:50px}
.news-date small{display:block;font-size:9px;font-weight:600;line-height:10px;margin-left:-2px}
.news-text{font-size:9.5px;line-height:12px;width:130px;padding-top:4px}
.news-text span{display:block;margin-top:14px;font-size:8.5px;font-weight:700}
.news .btn{position:absolute;left:540px;top:226px}

/* clients */
.clients{top:1809px;height:368px}
.clients .band-title{top:34px;color:var(--ink)}
.clients .band-title::after{background:var(--ink)}
.card{position:absolute;top:103px;width:222px;height:197px;border:1px solid #ccc;text-align:center;padding:26px 18px 0}
.card h3{font-size:15px;font-weight:400;color:var(--ink)}
.card h3 b{font-weight:800}
.card .role{font-size:11px;font-weight:700;color:var(--ink);margin:4px 0 18px}
.card p{font-size:9.5px;line-height:12px;color:#444;margin-bottom:10px}
.card b{font-weight:800}
.clients .dots{left:580px;top:335px}
.clients .dots i{background:var(--ink)}

/* terms */
.terms{top:2177px;height:223px}
.terms .dark-photo{background:linear-gradient(90deg,#2a2624,#3e3631 50%,#2a2624)}
.terms h2{position:absolute;top:36px;width:1200px;text-align:center;font-size:24px;font-weight:400;color:var(--white)}
.terms h2 b{font-weight:800}
.terms p{position:absolute;left:270px;width:660px;top:110px;text-align:center;color:var(--white);font-size:11px;line-height:18.5px}
.terms p b{font-weight:800}

/* map */
.map{top:2400px;height:232px;background:linear-gradient(135deg,#e9e6df,#dcd8cf 50%,#e6e3dc)}

/* footer */
.site-footer{top:2632px;height:232px;background:var(--foot)}
.foot-col{position:absolute;top:56px;color:#aaa;font-size:10px}
.foot-col h4{font-size:12px;font-weight:700;color:var(--white);margin-bottom:20px}
.foot-col li{list-style:none;line-height:22px}
.foot-post{width:180px;line-height:12px;margin-bottom:12px}
.foot-post span{display:block;color:var(--white);font-weight:700;font-size:8.5px;margin-top:4px}
.foot-contact{line-height:16px}
.foot-contact strong{color:#ccc;font-weight:500}
.bottom-bar{top:2864px;height:39px;background:var(--foot-bar);color:var(--white);font-size:9.5px}
.bottom-bar span{position:absolute;top:14px}
</style>
</head>
<body>

<header class="section site-header">
  <div class="brand">MORAVIA &amp; ZAMMIT</div>
  <div class="contact-bit contact-phone">
    <svg viewBox="0 0 24 24"><path d="M6.6 10.8c1.4 2.8 3.8 5.1 6.6 6.6l2.2-2.2c.3-.3.7-.4 1-.2 1.1.4 2.3.6 3.6.6.6 0 1 .4 1 1V20c0 .6-.4 1-1 1C10.6 21 3 13.4 3 4c0-.6.4-1 1-1h3.5c.6 0 1 .4 1 1 0 1.2.2 2.4.6 3.6.1.3 0 .7-.2 1z"/></svg>
    <div>(356) 2100 4400<br>hello@mzlegal.mt</div>
  </div>
  <div class="contact-bit contact-address">
    <svg viewBox="0 0 24 24"><path d="M12 3 2 12h3v8h5v-6h4v6h5v-8h3z"/></svg>
    <div>12/4, Harbour Lane, Valletta<br>88, Orchard Road, Birkirkara</div>
  </div>
</header>

<nav class="section main-nav">
  <ul>
    <li>HOME</li>
    <li>ABOUT US<span class="caret">▼</span></li>
    <li>PRACTICE AREAS<span class="caret">▼</span></li>
    <li>ABOUT MALTA</li>
    <li>CONTACT US</li>
  </ul>
  <div class="social"><span></span><span></span><span></span><span></span></div>
</nav>

<ul class="dropdown">
  <li>OUR FIRM</li>
  <li>OUR VALUES</li>
  <li>WHAT OTHERS SAY</li>
  <li>OFFICES</li>
</ul>

<section class="section hero">
  <div class="hero-photo" role="img" aria-label="Team of lawyers in business suits standing in an office"></div>
  <div class="hero-shade"></div>
  <div class="hero-copy">
    <h1>MORAVIA &amp; ZAMMIT</h1>
    <ul>
      <li>› Citizenship &amp; Residence</li>
      <li>› Overseas Patron Scheme</li>
      <li>› Arbitration and ADR</li>
      <li>› Commercial and Corporate</li>
      <li>› Media Law</li>
    </ul>
  </div>
  <span class="btn">LEARN MORE</span>
  <div class="dots"><i></i><i></i><i></i><i></i></div>
</section>

<section class="section welcome">
  <div class="welcome-photo" role="img" aria-label="Lawyers meeting around a conference table with laptops"></div>
  <div class="copy-col">
    <div class="eyebrow">WELCOME TO</div>
    <div class="section-name">MORAVIA &amp; ZAMMIT</div>
    <p class="body-copy">Vivamus finibus nisi non sapien viverra faucibus. Nam tempor purus arcu, non ullamcorper elit venenatis. In ut magna vel neque venenatis sed viverra est. Etiam volutpat non libero consequat vehicula dolor eu aliquet nulla eu ante maximus. Aliquam erat volutpat tincidunt elementum placerat elit. Donec finibus mi purus.</p>
    <p class="body-copy">Phasellus convallis at purus auctor, iaculis tempus met a laoreet nulla. Nulla malesuada mauris diam, sed fermentum luctus vel lectus mi suscipit ullamcorper quis. Fusce vestibulum dui ligula pellentesque nulla eget hendrerit. Ut ac tincidunt sapien. Mauris elementum placerat felis.</p>
    <span class="btn">VIEW OUR <b>CASES</b></span>
  </div>
</section>

<section class="section practice">
  <div class="dark-photo" role="img" aria-label="Scales of justice on a desk in warm dark light"></div>
  <h2 class="band-title">VIEW OUR <b>PRACTICE AREAS</b></h2>
  <p class="practice-lead">Practice Areas: Criminal, Citizenship &amp; Residence, Overseas Patron Scheme, Criminal Defence, Civil Litigation, Arbitration and ADR, Commercial and Corporate, Media Law.</p>
  <p class="practice-more"><b>Phasellus convallis at purusauctor,</b> iaculis tempus met a <b>laoreet nulla. Null</b>a maleda mauris dammentum <b>lufaucibus vlips</b> diam, sed <b>umc lectus mi</b>, susco <b>lnulla at pu</b> convallis at <b>purus auctorelir,</b> mauris diam, sed <b>tepus met a laoreella.</b> Nulla <b>lesuuris</b> maurisam, sed <b>nullesua.</b></p>
  <span class="btn on-dark">VIEW OUR <b>CASES</b></span>
</section>

<section class="section about">
  <div class="copy-col">
    <h2>ABOUT MALTA</h2>
    <div class="eyebrow">MORAVIA &amp; ZAMMIT</div>
    <p class="body-copy">Vivamus finibus nisi non sapien viverra faucibus. Nam tempor purus arcu, non ullamcorper elit venenatis. In ut magna vel neque venenatis sed viverra est. Etiam volutpat non libero consequat vehicula dolor eu aliquet nulla eu ante maximus. Aliquam erat volutpat tincidunt elementum placerat elit. Donec finibus mi purus.</p>
    <p class="body-copy">Phasellus convallis at purus auctor, iaculis tempus met a laoreet nulla. Nulla malesuada mauris diam, sed fermentum luctus vel lectus mi suscipit ullamcorper quis. Fusce vestibulum dui ligula pellentesque nulla eget hendrerit. Ut ac tincidunt sapien. Mauris elementum placerat felis.</p>
    <span class="btn">VIEW ABOUT <b>MALTA</b></span>
  </div>
  <div class="about-photo" role="img" aria-label="Lawyer in a dark suit standing by a bright office window"></div>
</section>

<section class="section news">
  <div class="dark-photo" role="img" aria-label="Gavel and law books on a dark wooden desk"></div>
  <h2 class="band-title">OUR LATEST <b>NEWS</b></h2>
  <div class="news-list">
    <div class="news-item">
      <div class="news-date">13<small>June 2016</small></div>
      <div class="news-text">Ipsum faucibus tempor purus arcu, quam elit venenatis at magna vel dolor ex aliquet.<span>Read More</span></div>
    </div>
    <div class="news-item">
      <div class="news-date">21<small>June 2016</small></div>
      <div class="news-text">Ipsum faucibus tempor purus arcu, quam elit venenatis at magna vel dolor ex aliquet.<span>Read More</span></div>
    </div>
    <div class="news-item">
      <div class="news-date">29<small>June 2016</small></div>
      <div class="news-text">Ipsum faucibus tempor purus arcu, quam elit venenatis at magna vel dolor ex aliquet.<span>Read More</span></div>
    </div>
  </div>
  <span class="btn on-dark">VIEW OUR <b>NEWS</b></span>
</section>

<section class="section clients">
  <h2 class="band-title">WHAT <b>CLIENTS SAY...</b></h2>
  <div class="card" style="left:248px">
    <h3>KARL <b>MIFSUD</b></h3>
    <div class="role">Supervisor</div>
    <p><b>MAURIS</b> et risus in ante auctor pretium. Proin euismod felis orci <b>SUSPENDISSE</b> ut volutpat leo. Aliquam feugiat massa eget libero rhoncus elementum a facilisis. In tincidunt convallis <b>PRETIUM</b> nec elit turpis.</p>
    <p>Fusce FRINGILLA hendrerit diam congue laoreet. Suspendisse sit amet <b>EGESTAS</b> justo.</p>
  </div>
  <div class="card" style="left:488px">
    <h3>RITA <b>BORG</b></h3>
    <div class="role">Commercial Driver</div>
    <p><b>MAURIS</b> et risus in ante auctor pretium. Proin euismod felis orci <b>SUSPENDISSE</b> ut volutpat leo. Aliquam feugiat massa eget libero rhoncus elementum a facilisis. In tincidunt convallis <b>PRETIUM</b> nec elit turpis.</p>
    <p>Fusce FRINGILLA hendrerit diam congue laoreet. Suspendisse sit amet <b>EGESTAS</b> justo.</p>
  </div>
  <div class="card" style="left:728px">
    <h3>PAUL <b>CAMILLERI</b></h3>
    <div class="role">Tractor Driver</div>
    <p><b>LIPSUM</b> et risus in ante auctor pretium. Proin euismod felis orci <b>Suspendisse</b> ut volutpat leo. Aliquam feugiat massa eget libero rhoncus elementum a facilisis. In tincidunt convallis <b>PRETIUM</b> nec elit turpis. Fusce FRINGILLA hendrerit diam congue laoreet. Suspendisse sit amet <b>EGESTAS</b> justo.</p>
  </div>
  <div class="dots"><i></i><i></i><i></i><i></i><i></i></div>
</section>

<section class="section terms">
  <div class="dark-photo" role="img" aria-label="Dim background of lawyers in conversation"></div>
  <h2><b>Terms</b> &amp; <b>Privacy</b> Statement</h2>
  <p><b>MAURIS</b> et risus in ante auctor <b>PRETIUM SUSPENDISSE.</b> Proin euismod felis orci <b>SUSPENDISSE</b> ut volutpat leo. Aliquam feugiat massa eget libero rhoncus elementum a facilisis. In feugiat massa eget libero rhoncus elementum a facilisis. <b>PRETIUM SUSPENDISSE</b> tincidunt convallis, <b>PRETIUM</b> nec elit feugiat massa <b>PRETIUM SUSPENDISSE</b> a facilisis. In tincidunt tincidunt convallis, <b>PRETIUM</b> nec elit turpis convallis, <b>PRETIUM</b> nec elit turpis sum posed.</p>
</section>

<section class="section map" role="img" aria-label="Street map of Valletta showing the office location"></section>

<footer class="section site-footer">
  <div class="foot-col" style="left:248px">
    <h4>Quick Links</h4>
    <ul><li>Home</li><li>About us</li><li>Practice Areas</li><li>About Malta</li><li>Contact Us</li></ul>
  </div>
  <div class="foot-col" style="left:372px">
    <h4>News Post</h4>
    <div class="foot-post">Lorem ipsum dolor sit amet. Lorem ipsum dolor sit amet, consect unt, consectetur sit amet.<span>2 day ago</span></div>
    <div class="foot-post">Lorem ipsum dolor sit amet. Lorem ipsum dolor sit amet, consect unt, consectetur sit amet.<span>2 day ago</span></div>
  </div>
  <div class="foot-col" style="left:584px">
    <h4>News Post</h4>
    <div class="foot-post">Lorem ipsum dolor sit amet. Lorem ipsum dolor sit amet, consect unt, consectetur sit amet.<span>2 day ago</span></div>
    <div class="foot-post">Lorem ipsum dolor sit amet. Lorem ipsum dolor sit amet, consect unt, consectetur sit amet.<span>2 day ago</span></div>
  </div>
  <div class="foot-col foot-contact" style="left:799px">
    <h4>Contact Us</h4>
    <strong>P.L. Marika Grech</strong><br>
    12/4, Harbour Lane, Valletta<br>
    88, Orchard Road, Birkirkara<br>
    Tel: (356) 2100 4411 (Valletta)<br>
    Tel: (356) 2100 4400 (Birkirkara)<br>
    Fax: (356) 2100 4499<br>
    Email: hello@mzlegal.mt
  </div>
</footer>

<div class="section bottom-bar">
  <span style="left:248px">© 2016, MORAVIA &amp; ZAMMIT. All rights reserved.</span>
  <span style="left:748px">Design &amp; Developed by NORTHPOINT STUDIO</span>
</div>

</body>
</html>
```